Retail Seafood business needs package/label design

In need of packaging/label design for multiple seafood products such as sword fish, halibut, cod fish, scallops, mahi, catfish, and lobster tails

```html
<!DOCTYPE html>
<html lang="en">
<head>
<meta charset="utf-8">
<title>Harbor Market Seafood Labels</title>
<link rel="stylesheet" href="https://fonts.googleapis.com/css2?family=Bebas+Neue&family=Caveat:wght@600&family=Josefin+Sans:wght@400;600;700&family=Quicksand:wght@500&display=swap">
<style>
  :root {
    --backdrop: #eefbb4;
    --navy: #3d4b82;
    --navy-deep: #34417a;
    --teal: #8dbcc8;
    --teal-pale: #c0e1e7;
    --cream: #ede6d2;
    --ink: #2c3868;
    --line: #9ccbd5;
    --fish-a: #6f8fb0;
    --fish-b: #4f6596;
  }
  * { box-sizing: border-box; margin: 0; padding: 0; }
  html, body { width: 1200px; height: 553px; overflow: hidden; }
  body { background: var(--backdrop); position: relative; font-family: "Josefin Sans", sans-serif; }

  .caption { position: absolute; font-family: "Quicksand", sans-serif; font-size: 10px; color: #1d1d1d; }
  .caption--with { left: 112px; top: 19px; }
  .caption--without { left: 971px; top: 468px; }

  .label { position: absolute; top: 58px; width: 194px; height: 380px; background: var(--navy); overflow: hidden; }
  .label--tuna { left: 33px; }
  .label--salmon-a { left: 343px; }
  .label--salmon-b { left: 653px; }
  .label--swordfish { left: 962px; }

  .frame { position: absolute; left: 16px; right: 16px; top: 16px; bottom: 120px; border: 0.6px solid var(--line); opacity: .7; }

  .badge { position: absolute; left: 42px; top: 8px; width: 110px; height: 110px; border-radius: 50%; background: var(--navy); border: 1px solid var(--line); display: flex; flex-direction: column; align-items: center; justify-content: center; text-align: center; }
  .badge__name { font-weight: 700; font-size: 13px; line-height: 1.05; color: var(--cream); letter-spacing: .5px; text-transform: uppercase; }
  .badge__tagline { margin-top: 8px; font-size: 3.3px; line-height: 1.5; letter-spacing: .3px; color: var(--cream); text-transform: uppercase; width: 60px; }

  .band { position: absolute; left: 0; right: 0; top: 131px; bottom: 0; background: var(--teal); }
  .band::before { content: ""; position: absolute; left: 0; right: 0; top: -5px; height: 6px;
    background: radial-gradient(circle at 4px 6px, var(--teal) 4px, transparent 4.5px) repeat-x; background-size: 8px 6px; }

  .title { position: absolute; left: 0; right: 0; top: 20px; text-align: center; font-family: "Bebas Neue", sans-serif; font-size: 27px; letter-spacing: .5px; color: var(--cream); line-height: 1; }
  .script { position: absolute; left: 0; right: 0; top: 40px; text-align: center; font-family: "Caveat", cursive; font-size: 20px; color: var(--ink); line-height: 1; }

  .info { position: absolute; left: 16px; right: 16px; top: 72px; height: 54px; background: var(--teal-pale); text-align: center; color: var(--ink); text-transform: uppercase; }
  .info::before { content: ""; position: absolute; left: 0; right: 0; top: -4px; height: 5px;
    background: radial-gradient(circle at 3px 5px, var(--teal-pale) 3px, transparent 3.5px) repeat-x; background-size: 6px 5px; }
  .info__line { display: block; font-size: 4.6px; letter-spacing: .4px; padding: 3px 0; }
  .info__line--rule { border-bottom: 0.5px solid var(--line); margin: 0 18px; }
  .info__line--big { font-size: 5.2px; }
  .info__small { display: block; font-size: 3.8px; line-height: 1.4; letter-spacing: .3px; margin-top: 3px; }

  .illustration { position: absolute; left: 0; right: 0; top: 126px; height: 52px; background: linear-gradient(100deg, var(--fish-a), var(--fish-b) 60%, var(--fish-a)); opacity: .85; }

  .footer { position: absolute; left: 0; right: 0; bottom: 0; height: 92px; background: var(--navy-deep); }
  .footer__name { position: absolute; right: 16px; top: 14px; font-weight: 700; font-size: 12px; color: var(--cream); letter-spacing: .4px; text-transform: uppercase; }
  .social { position: absolute; left: 18px; top: 48px; list-style: none; font-size: 5px; color: var(--cream); }
  .social li { display: flex; align-items: center; gap: 3px; margin-bottom: 3px; }
  .social li::before { content: ""; width: 5px; height: 5px; border-radius: 50%; background: var(--cream); }
  .address { position: absolute; right: 16px; top: 44px; text-align: right; font-style: normal; font-size: 5.3px; line-height: 1.45; letter-spacing: .3px; color: var(--cream); text-transform: uppercase; }
  .address .web { text-transform: none; }
</style>
</head>
<body>
  <p class="caption caption--with">with illustration</p>

  <!-- Yellowfin tuna label, illustrated -->
  <section class="label label--tuna">
    <div class="frame"></div>
    <div class="badge"><span class="badge__name">Harbor<br>Market</span><span class="badge__tagline">The Heartland's source of seafood &amp; produce for over 15 years</span></div>
    <div class="band">
      <h2 class="title">Yellowfin Tuna</h2>
      <p class="script">fresh seafood</p>
      <div class="info">
        <span class="info__line info__line--rule">Priced per pound</span>
        <span class="info__line info__line--big">Some of the best tuna you can eat</span>
        <span class="info__small">#1 sashimi grade<br>wild caught</span>
      </div>
      <div class="illustration" role="img" aria-label="Engraved illustration of tuna, fish and lobster"></div>
    </div>
    <footer class="footer">
      <p class="footer__name">Harbor Market</p>
      <ul class="social"><li>harbor market</li><li>@harbormarket</li><li>@harbormarket</li></ul>
      <address class="address">128 N. Lakeview Ave<br>Springfield, IL 62701<br>555-010-2847<br><span class="web">www.harbormarket.example/</span></address>
    </footer>
  </section>

  <!-- Salmon portions label, illustrated -->
  <section class="label label--salmon-a">
    <div class="frame"></div>
    <div class="badge"><span class="badge__name">Harbor<br>Market</span><span class="badge__tagline">The Heartland's source of seafood &amp; produce for over 15 years</span></div>
    <div class="band">
      <h2 class="title">Salmon Portions</h2>
      <p class="script">fresh seafood</p>
      <div class="info">
        <span class="info__line info__line--rule">(2) 8 oz portions</span>
        <span class="info__line info__line--big">Sashimi grade skinless Atlantic salmon</span>
        <span class="info__small">Sourced from responsible and<br>approved Norwegian salmon farms</span>
      </div>
      <div class="illustration" role="img" aria-label="Engraved illustration of fish and lobster"></div>
    </div>
    <footer class="footer">
      <p class="footer__name">Harbor Market</p>
      <ul class="social"><li>harbor market</li><li>@harbormarket</li><li>@harbormarket</li></ul>
      <address class="address">128 N. Lakeview Ave<br>Springfield, IL 62701<br>555-010-2847<br><span class="web">www.harbormarket.example/</span></address>
    </footer>
  </section>

  <!-- Salmon portions label, plain -->
  <section class="label label--salmon-b">
    <div class="frame"></div>
    <div class="badge"><span class="badge__name">Harbor<br>Market</span><span class="badge__tagline">The Heartland's source of seafood &amp; produce for over 15 years</span></div>
    <div class="band">
      <h2 class="title">Salmon Portions</h2>
      <p class="script">fresh seafood</p>
      <div class="info">
        <span class="info__line info__line--rule">(2) 8 oz portions</span>
        <span class="info__line info__line--big">Sashimi grade skinless Atlantic salmon</span>
        <span class="info__small">Sourced from responsible and<br>approved Norwegian salmon farms</span>
      </div>
    </div>
    <footer class="footer">
      <p class="footer__name">Harbor Market</p>
      <ul class="social"><li>harbor market</li><li>@harbormarket</li><li>@harbormarket</li></ul>
      <address class="address">128 N. Lakeview Ave<br>Springfield, IL 62701<br>555-010-2847<br><span class="web">www.harbormarket.example/</span></address>
    </footer>
  </section>

  <!-- Swordfish label, plain -->
  <section class="label label--swordfish">
    <div class="frame"></div>
    <div class="badge"><span class="badge__name">Harbor<br>Market</span><span class="badge__tagline">The Heartland's source of seafood &amp; produce for over 15 years</span></div>
    <div class="band">
      <h2 class="title" style="top:34px">Swordfish</h2>
      <p class="script" style="top:54px">frozen seafood</p>
      <div class="info" style="top:98px">
        <span class="info__line info__line--rule" style="padding-top:14px">(2) 8 oz portions</span>
        <span class="info__line info__line--rule">Wild caught</span>
      </div>
    </div>
    <footer class="footer">
      <p class="footer__name">Harbor Market</p>
      <ul class="social"><li>harbor market</li><li>@harbormarket</li><li>@harbormarket</li></ul>
      <address class="address">128 N. Lakeview Ave<br>Springfield, IL 62701<br>555-010-2847<br><span class="web">www.harbormarket.example/</span></address>
    </footer>
  </section>

  <p class="caption caption--without">no illustration</p>
</body>
</html>
```